Cool cafe needs help with our corporate identity.

We have a logo! We have a font!

What we need is to tie it together for
1. A menu
2. Labels for jam and other things we sell
3. Business Cards

All should have the same design style.

We have a strong design aesthetic in the cafe. Lots of colour and quirky objects. See this Snapvale profile for photos (you can download high-res from here if you sign into Snapvale): http://www.snapvale-example.net/photos/51827094@K03/

Also our website is www.peterwalrus.net

A main feature is the counter that is made of yardsticks.

There is also a bit of and 80's feel. Especially images of Edmund and Bea (the Royals).

We also like weird taxidermy and anthropology images from the 1920s. Harold P. Quimsby was an anthropologist who used to own a Walrus called Peter. That is where our name comes from. Seekly 'Harold P. Quimsby' for interesting images.

Perhaps design elements could be taken from any of these themes, although we are open to other ideas.

We like being playful and irreverent.

The logo is the words Peter Walrus in Cursive. We want to stick with that. The font we like is Tallow Works Voss. The logo is currently blue colour - this can change.

1.Menu Specs
We like printing this ourselves. Thick paper A4 with a fold seems to work well. We want some design elements added. Our existing menu is attached.

2. Labels
We have jam jars and labels for biscuits. These are various sizes. It needs to have the name of the jam,e.g. Apricot, The Peter Walrus Logo, Some design elements, A list of ingredients, and the weight. Eg 250g.

3. Business Card
A standard sized business card with The logo, design elements and the following words:
Peter Walrus Cafe
17 Lindqvist Road, Brunswick West
03 9017 4426
www.peterwalrus.net

Target Market(s)

Adults based in Melbourne, Australia that like design and are kind of hipsterish,

Industry/Entity Type

Printing

Requirements
Must have
• Logo and font as described.
Nice to have
• Maybe a bit quirky.
Should not have
• Slick corporate look.

```html
<!DOCTYPE html>
<html lang="en">
<head>
<meta charset="utf-8">
<title>Peter Walrus – Menu</title>
<link rel="stylesheet" href="https://fonts.googleapis.com/css2?family=Libre+Caslon+Text:ital,wght@0,400;0,700;1,400;1,700&family=Varela+Round&display=swap">
<style>
  :root {
    --paper: #efe7d6;
    --paper-line: #e2d7c2;
    --ink: #2a2623;
    --rule: #7d756c;
    --cereals: #b2304f;
    --breakfast: #d68c5c;
    --eggs: #e2691f;
    --sandwiches: #5e7b4c;
    --salad: #5e6d95;
    --kids: #97a85b;
    --drinks: #9b3c4f;
    --badge: #1a9ed9;
    --tag-vg: #e2287c;
    --tag-v: #19a1d9;
    --tag-gf: #f08d2b;
  }
  * { box-sizing: border-box; margin: 0; padding: 0; }
  html, body { width: 848px; height: 1200px; overflow: hidden; }
  body {
    position: relative;
    background: var(--paper);
    color: var(--ink);
    font-family: "Libre Caslon Text", Georgia, serif;
    font-size: 14.5px;
    line-height: 21px;
  }
  .column { position: absolute; top: 0; width: 352px; height: 1200px; }
  .column--left { left: 37px; }
  .column--right { left: 461px; }
  .brand {
    position: absolute; top: 52px; left: 0; width: 100%;
    text-align: center; font-size: 26px; line-height: 30px;
    font-weight: 400; color: var(--ink);
  }
  .section { position: absolute; left: 0; width: 100%; }
  .section__title {
    height: 22px; padding-left: 8px;
    color: #fff; font-weight: 700; font-size: 16px; line-height: 23px;
  }
  .section__items { list-style: none; padding: 4px 8px 0 8px; }
  .item {
    display: grid; grid-template-columns: 1fr auto; align-items: end;
    column-gap: 8px; margin-bottom: 6px;
  }
  .item__price { text-align: right; }
  .item em { font-style: italic; font-weight: 700; }
  .section__items--tight .item { margin-bottom: 5px; }
  .section__items--drinks .item { margin-bottom: 5px; }
  .title--cereals { background: var(--cereals); }
  .title--breakfast { background: var(--breakfast); }
  .title--eggs { background: var(--eggs); }
  .title--sandwiches { background: var(--sandwiches); }
  .title--salad { background: var(--salad); }
  .title--kids { background: var(--kids); }
  .title--drinks { background: var(--drinks); }
  .notes {
    position: absolute; top: 1053px; left: 0; width: 100%;
    border-top: 1px solid var(--rule); border-bottom: 1px solid var(--rule);
    padding: 4px 0 5px; text-align: center; font-size: 14.5px; line-height: 20.5px;
  }
  .legend {
    position: absolute; top: 1153px; left: 0; width: 100%;
    display: flex; justify-content: space-between; font-size: 14.5px;
  }
  .legend__tag {
    display: inline-block; padding: 0 4px; margin-right: 4px;
    color: #fff; font-style: italic; font-weight: 700; line-height: 20px;
  }
  .tag--vg { background: var(--tag-vg); }
  .tag--v { background: var(--tag-v); }
  .tag--gf { background: var(--tag-gf); }
  .decor-still-life { position: absolute; left: 0; top: 1040px; }
  .coffee-badge {
    position: absolute; left: 214px; top: 1102px; width: 196px; height: 72px;
    background: var(--badge); color: #fff; transform: rotate(8deg);
    font-family: "Varela Round", Arial, sans-serif; font-size: 15px; line-height: 20px;
    text-align: center; padding-top: 14px;
  }
</style>
</head>
<body>

<svg class="decor-still-life" width="260" height="160" viewBox="0 0 260 160" role="img" aria-label="Still life of pink flowers in glass bottles beside a wooden yardstick">
  <rect x="0" y="0" width="80" height="160" fill="#d9cfc2"/>
  <polygon points="0,112 260,150 260,160 0,160" fill="#e3c25a"/>
</svg>

<div class="column column--left">
  <div class="brand">peter walrus</div>

  <section class="section" style="top:103px">
    <h2 class="section__title title--cereals">Cereals, Fruit and Toast</h2>
    <ul class="section__items">
      <li class="item"><span>Seasonal <em>fruit salad</em>, leatherwood<br>honey labne, mint, pistachio <em>(v,gf)</em></span><span class="item__price">11.5</span></li>
      <li class="item"><span>Maple toasted spiced <em>granola</em>,<br>seasonal fruit compote,<br>milk of choice <em>(vg)</em></span><span class="item__price">11.5</span></li>
      <li class="item"><span>Add honey labne</span><span class="item__price">12.5</span></li>
      <li class="item"><span>Rolled-oats <em>porridge</em>,<br>dates,banana, creamed honey <em>(v)</em></span><span class="item__price">11.5</span></li>
      <li class="item"><span>Peter Walrus’s <em>bircher muesli</em>,<br>raisin, hazelnut with<br>seasonal fruit <em>(v)</em></span><span class="item__price">11.5</span></li>
      <li class="item"><span>Casa Forno’s <em>toasts</em><br>(sourdough/ multi-grain/ fruit<br>toast/FreeRise gluten-free)</span><span class="item__price">6.5</span></li>
    </ul>
  </section>

  <section class="section" style="top:455px">
    <h2 class="section__title title--breakfast">Breakfast</h2>
    <ul class="section__items">
      <li class="item"><span>Brioche <em>french toast</em>, earl-grey<br>poached pear, candied walnuts,<br>white chocolate mousse <em>(v)</em></span><span class="item__price">16.5</span></li>
      <li class="item"><span><em>Coconut crepes</em>, rosemary grilled<br>pineapple, vanilla mascarpone <em>(v)</em></span><span class="item__price">16.5</span></li>
      <li class="item"><span><em>Aloo sabji</em>-dry curry of potato,<br>mustard oil, black cumin, fried<br>eggs, coriander, raita <em>(v,gf*)</em></span><span class="item__price">17.5</span></li>
      <li class="item"><span><em>Big Peter’s breakfast</em>-eggs of your<br>choice, grilled black pudding,<br>bacon, tomato, salsa verde</span><span class="item__price">19</span></li>
      <li class="item"><span>Braised black <em>beans</em>, capsicum,<br>tomato, and cornbread crumble <em>(v)</em></span><span class="item__price">16.5</span></li>
      <li class="item"><span>Five-spiced pork <em>omelette</em>,<br>bean sprouts, asian herb salad</span><span class="item__price">18</span></li>
    </ul>
  </section>

  <section class="section" style="top:827px">
    <h2 class="section__title title--eggs">Eggs</h2>
    <ul class="section__items">
      <li class="item"><span>Eggs of your choice (poached,<br>scrambled, fried) served on toast</span><span class="item__price">9</span></li>
      <li class="item"><span>Sides:</span><span></span></li>
      <li class="item"><span>hollandaise/salsa verde/dukkah/<br>tomato chutney/extra egg</span><span class="item__price">2.5 each</span></li>
      <li class="item"><span>roasted tomato/avocado/spinach/<br>baked beans/field mushrooms</span><span class="item__price">3.5 each</span></li>
      <li class="item"><span>bacon/black pudding/<br>Marlow goat’s cheese/<br>smoked salmon/kransky</span><span class="item__price">4.5 each</span></li>
    </ul>
  </section>
</div>

<div class="coffee-badge">Ask about our Single<br>Origin Coffee</div>

<div class="column column--right">
  <div class="brand">peter walrus</div>

  <section class="section" style="top:103px">
    <h2 class="section__title title--sandwiches">Sandwiches</h2>
    <ul class="section__items">
      <li class="item"><span>Smoked salmon <em>bagel</em>, goats curd,<br>capers, red onion, cucumber<br>and beetroot relish</span><span class="item__price">12.5</span></li>
      <li class="item"><span><em>B.L.A.T</em>- Bacon, lettuce,<br>avocado, lettuce and aioli</span><span class="item__price">12.5</span></li>
      <li class="item"><span>Leg ham, gouda, red onion jam<br>toasted sandwich</span><span class="item__price">12.5</span></li>
      <li class="item"><span>12-hours braised <em>beef brisket</em>,<br>cheddar, Peter Walrus’s BBQ<br>sauce, pickled peppers</span><span class="item__price">13.5</span></li>
    </ul>
  </section>

  <section class="section" style="top:361px">
    <h2 class="section__title title--salad">Salad</h2>
    <ul class="section__items">
      <li class="item"><span>House cured <em>tuna</em>, <em>burghul</em>,<br>preserved lemon, peas,<br>mint and parsley</span><span class="item__price">17.5</span></li>
      <li class="item"><span><em>Soba</em>, cucumber, tatsoi,<br>spring onion, pickled cabbage,<br>sesame dressing <em>(vg)</em></span><span class="item__price">16.5</span></li>
    </ul>
  </section>

  <section class="section" style="top:525px">
    <h2 class="section__title title--kids">Kids (under 12)</h2>
    <ul class="section__items section__items--tight">
      <li class="item"><span>Cheese and ham toastie</span><span class="item__price">6.5</span></li>
      <li class="item"><span>Single poached egg on toast</span><span class="item__price">6.5</span></li>
      <li class="item"><span>French toast and maple syrup</span><span class="item__price">6.5</span></li>
    </ul>
  </section>

  <section class="section" style="top:633px">
    <h2 class="section__title title--drinks">Drinks</h2>
    <ul class="section__items section__items--drinks">
      <li class="item"><span>Ombra coffee</span><span class="item__price">4</span></li>
      <li class="item"><span>Single origin 4 Espresso</span><span class="item__price">3.5</span></li>
      <li class="item"><span>Babycino</span><span class="item__price">1</span></li>
      <li class="item"><span>Hot chocolate</span><span class="item__price">4</span></li>
      <li class="item"><span>Chai with soy milk &amp; honey</span><span class="item__price">5.5</span></li>
      <li class="item"><span>Fenwick &amp; Gray teas- black<br>and herbal all</span><span class="item__price">4</span></li>
      <li class="item"><span>Iced coffee</span><span class="item__price">5.5</span></li>
      <li class="item"><span>Iced chocolate</span><span class="item__price">5.5</span></li>
      <li class="item"><span>Organic orange juice</span><span class="item__price">5</span></li>
      <li class="item"><span>Organic apple juice</span><span class="item__price">5</span></li>
      <li class="item"><span>Organic grapefruit juice</span><span class="item__price">5</span></li>
      <li class="item"><span>Kestrel Springs: Small<br>Kestrel Springs: Large</span><span class="item__price">4<br>5</span></li>
      <li class="item"><span>Mango Lassi</span><span class="item__price">5</span></li>
    </ul>
  </section>

  <p class="notes">We will try to accommodate variations<br>to our menu &amp; the splitting of bills,<br>however this may not always be possible.<br>EFPOS available</p>

  <div class="legend">
    <span><span class="legend__tag tag--vg">vg:</span>vegan</span>
    <span><span class="legend__tag tag--v">v:</span>vegetarian</span>
    <span><span class="legend__tag tag--gf">gf:</span>gluten free</span>
  </div>
</div>

</body>
</html>
```